Redesign of current website

Redesign - tmrdbllc.com

Coding

Coded - Design and coding required

Number of Pages Required

4 page

Colors

Designer to choose colors to be used in the design.

```html
<!DOCTYPE html>
<html lang="en">
<head>
<meta charset="utf-8">
<title>TMRDB, LLC – Safety &amp; Security</title>
<link href="https://fonts.googleapis.com/css2?family=Red+Hat+Display:wght@400;500;700;900&family=Roboto:wght@300;400;500&display=swap" rel="stylesheet">
<style>
:root{
  --black:#0b0b0b;
  --ink:#222;
  --text:#3a3a3a;
  --green:#1fa51f;
  --green-bright:#2fc42f;
  --green-deep:#118c11;
  --panel:#eef0f1;
  --white:#fff;
  --muted:#bdbdbd;
}
*{margin:0;padding:0;box-sizing:border-box}
html,body{width:1200px;height:2533px;overflow:hidden;background:var(--white)}
body{position:relative;font-family:"Roboto",sans-serif;color:var(--text)}
.abs{position:absolute}
.head{font-family:"Red Hat Display",sans-serif;color:var(--ink)}

.topbar{left:0;top:0;width:1200px;height:35px;background:var(--black);color:var(--white);font-size:10px}
.topbar .contact{left:173px;top:11px;display:flex;gap:20px;align-items:center}
.topbar .contact span{display:flex;align-items:center;gap:5px}
.topbar .login{right:173px;top:11px;font-family:"Red Hat Display",sans-serif;font-weight:700;display:flex;gap:8px;align-items:center}
.sq{width:7px;height:7px;background:var(--white);display:inline-block}

.site-header{left:0;top:35px;width:1200px;height:63px;background:var(--white);border-bottom:1px solid #e5e5e5}
.brand{font-family:"Red Hat Display",sans-serif;font-weight:900;color:var(--green);font-size:22px;left:173px;top:17px;display:flex;align-items:center;gap:7px}
.brand i{width:12px;height:12px;border-radius:50%;background:var(--green);display:inline-block}
.nav{right:173px;top:25px;display:flex;gap:21px;font-family:"Red Hat Display",sans-serif;font-size:10px;font-weight:500;color:var(--ink);letter-spacing:.2px}

.hero{left:0;top:98px;width:1200px;height:523px;background:radial-gradient(ellipse at 40% 55%,#3ad13a 0%,#27b527 45%,#1c9a1c 100%)}
.hero-photo{left:500px;top:0;width:570px;height:523px;background:linear-gradient(180deg,rgba(40,70,140,.0) 0%,rgba(34,58,120,.55) 30%,rgba(30,52,110,.8) 100%);border-radius:200px 200px 0 0}
.hero h1{left:173px;top:140px;color:var(--white);font-family:"Red Hat Display",sans-serif;line-height:1}
.hero h1 .l1{display:block;font-size:76px;font-weight:900;letter-spacing:1px}
.hero h1 .l2{display:block;font-size:60px;font-weight:400;margin-top:2px;letter-spacing:1px}
.hero h1 .l3{display:block;font-size:29px;font-weight:700;margin-top:10px}
.btn{background:var(--black);color:var(--white);font-family:"Red Hat Display",sans-serif;font-weight:700;letter-spacing:1.5px;display:flex;align-items:center;justify-content:center}
.hero .btn{left:174px;top:343px;width:181px;height:45px;font-size:16px}

.divider{left:0;width:1200px;display:flex;justify-content:center}
.section-title{left:0;width:1200px;text-align:center;font-weight:700;font-size:32px;line-height:43px}
.lead{left:230px;width:740px;text-align:center;font-size:11.5px;line-height:17px}

.col-photo{left:173px;top:936px;width:430px;height:311px;background:linear-gradient(180deg,#ececec,#d5d5d5)}
.overview h2{left:173px;top:1262px;font-size:32px;font-weight:700}
.overview p{left:173px;top:1306px;width:435px;font-size:10.8px;line-height:17px;font-weight:300;color:var(--ink)}
.overview .btn{left:173px;top:1385px;width:129px;height:31px;font-size:12px}

.info-panel{left:617px;top:939px;width:411px;height:474px;background:linear-gradient(120deg,#e7e9ea 0%,#f6f7f7 60%,#eceeef 100%)}
.info-panel .block{position:absolute;left:20px;width:372px}
.info-panel h3{font-family:"Red Hat Display",sans-serif;font-weight:700;font-size:31px;line-height:35px}
.info-panel p{font-size:10.5px;line-height:17px;font-weight:300;color:var(--ink);margin-top:10px}
.info-panel h3.dark{color:var(--ink)}
.info-panel h3.accent{color:var(--green)}

.band{left:0;top:1518px;width:1200px;height:475px;background:radial-gradient(ellipse at 50% 40%,#1fb81f 0%,#0f9e0f 60%,#0a8a0a 100%)}
.band .section-title{color:var(--white);top:80px}
.band .lead{color:var(--white);top:135px;left:225px;width:750px;font-weight:500;font-size:11.5px}
.product{left:330px;top:237px;width:540px;height:220px;background:linear-gradient(180deg,#d7dadc,#a9adb0);border-radius:60px 20px 30px 30px}

.partners .logos{left:225px;top:2150px;width:750px;display:flex;justify-content:space-between;align-items:center}
.badge{height:34px;background:#c9c9c9;border-radius:4px}

.footer{left:0;top:2257px;width:1200px;height:276px;background:var(--black);color:var(--white)}
.footer .brand{left:173px;top:32px;color:var(--white);font-size:26px}
.footer .brand i{background:var(--white)}
.footer .about{left:175px;top:120px;width:230px;font-size:10.5px;line-height:17px}
.footer h4{font-family:"Red Hat Display",sans-serif;font-weight:700;font-size:15px}
.footer ul{list-style:none;font-size:10px;line-height:19.5px;margin-top:8px}
.col-company{left:439px;top:44px}
.col-contact{left:607px;top:44px}
.col-follow{left:905px;top:44px}
.social{display:flex;gap:3px;margin-top:12px}
.social span{width:27px;height:27px;border-radius:50%;background:#5a5a5a}
.footer .rule{left:0;top:213px;width:1200px;height:1px;background:#222}
.copyright{left:0;top:237px;width:1200px;text-align:center;font-size:10px}
</style>
</head>
<body>

<div class="topbar abs">
  <div class="contact abs">
    <span><svg width="9" height="9" viewBox="0 0 10 10"><path d="M2 1l2 2-1 1.5c.6 1.2 1.3 1.9 2.5 2.5L7 6l2 2-1.2 1.5C4.5 9.3.7 5.5.5 2.2z" fill="#fff"/></svg>Phone: +1 (555) 014-2290</span>
    <span><svg width="11" height="8" viewBox="0 0 11 8"><rect x=".5" y=".5" width="10" height="7" fill="none" stroke="#fff"/><path d="M.5 .5l5 4 5-4" fill="none" stroke="#fff"/></svg>contact@tmrdbllc.com</span>
  </div>
  <div class="login abs"><span class="sq"></span><span class="sq"></span>LOGIN</div>
</div>

<header class="site-header abs">
  <div class="brand abs"><i></i>TMRDB</div>
  <nav class="nav abs"><span>HOME</span><span>COMPANY OVERVIEW</span><span>WHO ARE WE</span><span>OUR PARTNERS AND CLIENTS</span><span>CONTACT US</span></nav>
</header>

<section class="hero abs">
  <div class="hero-photo abs" role="img" aria-label="Technician in blue cap and work jacket holding up a dome security camera"></div>
  <h1 class="abs"><span class="l1">SAFETY</span><span class="l2">&amp; SECURITY</span><span class="l3">AT YOUR FINGER PRINTS</span></h1>
  <div class="btn abs">LEARN MORE</div>
</section>

<div class="divider abs" style="top:666px">
  <svg width="100" height="20" viewBox="0 0 100 20"><line x1="0" y1="10" x2="26" y2="10" stroke="#bbb"/><line x1="74" y1="10" x2="100" y2="10" stroke="#bbb"/><g fill="#222"><path d="M33 7l24-5 2 7-24 5z"/><rect x="55" y="10" width="3" height="8"/><rect x="55" y="16" width="10" height="2"/></g></svg>
</div>
<h2 class="section-title head abs" style="top:706px">TRI-MARK DEFENSE SOLUTIONS<br>GROUP, LLC (TMRDB, LLC)</h2>
<p class="lead abs" style="top:812px">We are a Self-certified Small Disabled Veteran Owned Business headquartered in Marlow, Georgia, the Home of the Infantry. We support our clients by supporting security, training and operational needs by using the experience gained through our military service in special operations and advance infantry tactics. Our company was established based upon the success of propelling other organizations to reach their full potential. Experience has also shown us that rewarding employee for their hard work, loyalty, and dedication will have a positive impact and influence on the overall company as a whole!</p>

<div class="col-photo abs" role="img" aria-label="Three white bullet surveillance cameras mounted on a pale wall"></div>
<div class="overview">
  <h2 class="head abs">COMPANY OVERVIEW</h2>
  <p class="abs">“A complete camera technical service company that installs, monitors, repairs, manage and maintain surveillance cameras for the government (military sources) and commercial clients. We provide our own team of highly skilled technicians for continuous consultation, training, and support.”</p>
  <div class="btn abs">VIEW OUR STORE</div>
</div>

<div class="info-panel abs">
  <div class="block" style="top:29px">
    <h3 class="dark">SERVICES AND<br>PRODUCTS</h3>
    <p>Technical Services: Surveillance camera installations, training and maintenance. Logistical Services: Supply management systems to include inventory, accountability, shipping, receiving and warehouse storage. Product Marketing Services: Research and procurement of camera systems, system software, network switches, routers, radios and power supplies.</p>
  </div>
  <div class="block" style="top:218px">
    <h3 class="accent">MISSION STATEMENT</h3>
    <p>TMRDB, LLC provides premier technology systems intergrades and services in our market, engaging the best talents and strong returns to support our customers missions, our communities and our Nation Management team</p>
  </div>
  <div class="block" style="top:339px">
    <h3 class="accent">OUR VALUES</h3>
    <p>Our core and moral values are what our company operates within trust, loyalty and integrity in the conduct of daily operations of business with our customers, partners and investors.</p>
  </div>
</div>

<section class="band abs">
  <div class="divider abs" style="top:33px">
    <svg width="100" height="20" viewBox="0 0 100 20"><line x1="0" y1="10" x2="26" y2="10" stroke="#fff"/><line x1="74" y1="10" x2="100" y2="10" stroke="#fff"/><g fill="#fff"><path d="M33 7l24-5 2 7-24 5z"/><rect x="55" y="10" width="3" height="8"/><rect x="55" y="16" width="10" height="2"/></g></svg>
  </div>
  <h2 class="section-title head abs">SURVEILLANCE CAMERAS SYSTEM</h2>
  <p class="lead abs">The Orion is a revolutionary multi-sensor PTZ camera boasting a long-range 33X visible day/night camera, long-range thermal infrared zoom, and ZLID NIR illumination with LRF. This multi-sensor payload enables the Orion to provide high-resolution imaging in virtually any environment from fog to complete darkness. Designed for accurate positioning of weapons systems, the pan/tilt unit meets and exceeds MIL-STD-810F military ratings for shock, vibration, temperature and dust/ water ingression. This makes the Orion the ultimate long-range camera system for 24/7 situational awareness and long-range recognition and identification of targets.</p>
  <div class="product abs" role="img" aria-label="Silver multi-sensor pan/tilt camera unit with thermal lens and optical camera pods"></div>
</section>

<div class="divider abs" style="top:2048px">
  <svg width="100" height="20" viewBox="0 0 100 20"><line x1="0" y1="10" x2="26" y2="10" stroke="#bbb"/><line x1="74" y1="10" x2="100" y2="10" stroke="#bbb"/><g fill="#222"><path d="M33 7l24-5 2 7-24 5z"/><rect x="55" y="10" width="3" height="8"/><rect x="55" y="16" width="10" height="2"/></g></svg>
</div>
<h2 class="section-title head abs" style="top:2097px">OUR PARTNERS</h2>
<div class="partners">
  <div class="logos abs">
    <span class="badge" style="width:130px" aria-label="Partner badge"></span>
    <span class="badge" style="width:136px" aria-label="Partner badge"></span>
    <span class="badge" style="width:118px;height:40px" aria-label="Partner badge"></span>
    <span class="badge" style="width:136px;height:24px" aria-label="Partner badge"></span>
    <span class="badge" style="width:94px" aria-label="Partner badge"></span>
  </div>
</div>

<footer class="footer abs">
  <div class="brand abs"><i></i>TMRDB</div>
  <p class="about abs">We are a Self-certified Small Disabled Veteran Owned Business headquartered in Marlow, Georgia, the Home of the Infantry.</p>
  <div class="col-company abs">
    <h4>Company</h4>
    <ul><li>Home</li><li>Company Overview</li><li>Our Partners and CLIENTS</li><li>Who Are We</li><li>Contact</li></ul>
  </div>
  <div class="col-contact abs">
    <h4>Contact</h4>
    <ul style="line-height:17.5px"><li>Tri-Mark Defense Solutions Group, LLC (TMRDB, LLC)</li><li>1420 Ridgeline Road Marlow, GA 31000</li><li>Daniel Pryor +1 (555) 014-7731</li><li>contact@tmrdbllc.com</li><li>www.tmrdbllc.com</li></ul>
  </div>
  <div class="col-follow abs">
    <h4>Follow Us</h4>
    <div class="social"><span aria-label="Social link"></span><span aria-label="Social link"></span><span aria-label="Social link"></span></div>
  </div>
  <div class="rule abs"></div>
  <p class="copyright abs">© 2020 TMRDB, LLC,All Rights Reserved.</p>
</footer>

</body>
</html>
```